Thornwick Meadows Organic Hemp Company needs an OLD WORLD Label for CBD Bottle!

*UPDATE* Increased the budget! Please keep in mind, we are also open to "modern vintage", "hipster vintage" and other forms of retro emulation. Whatever the case, we are looking for a small work of art, like an indie Gin bottle- not the clinical drab that every other CBD bottle has. Also, don't be afraid to incorporate color, or alter the logo (color wise), we want something breathtaking in a small package. Show us what that looks like to you!

*UPDATE* Please take a moment to visit this link to see the types of branding we are interested in: https://www.pinboardly.example/gregorpaulwexford/tidy-branding/

We are an Organic Hemp company about to launch it's first line of products. This design is for our CBD Bottle. We have a pre-existing logo that we need developed and expanded into a label. Our theme is Old World, Victorian, Vintage, Turn of the Century (there are too many names for this genre, you get it...) We want our brand to convey a sense of intrigue, artisan quality and a bit of mystery. Very different from the clinical look of most CBD tinctures. We are HUGE fans of the design house "Holloway and Quince" and would LOVE something that conjures that feel.

The first attachment will be our current logo, and I will be adding "inspiration" as I can.

The second attachment will be a rendition of our raw logo with regulatory information. This is what we need this spiced up! You DO NOT have to follow this design, but the same information needs to be on there. It's very likely that the line work will be in "gold foil".

Any additional attachments are for "inspiration", what we're looking for.

Feel free to explore with it, we are looking for something breathtaking!

Thanks!

Gregor
Thornwick Meadows
Verdant Curios

Target Market(s)

Younger, Hipster Demographic and all who are interested in Organic Products!

Colors

Designer to choose colors to be used in the design.

Requirements
Must have
• Full Spectrum Hemp Extract CDB Oil 1000mg Natural Flavor 1.02 FL OZ (30 ML)
Should not have
• Cannabis, Cannabis leaves, Marijuana etc...

```html
<!DOCTYPE html>
<html lang="en">
<head>
<meta charset="utf-8">
<title>Thornwick Meadows – CBD Oil Label</title>
<link rel="stylesheet" href="https://fonts.googleapis.com/css2?family=Cinzel:wght@500;700&family=Old+Standard+TT:wght@400;700&family=Playfair+Display:wght@800&display=swap">
<style>
  :root {
    --paper: #ffffff;
    --label-black: #0e0d0c;
    --gold: #b3913f;
    --gold-deep: #7d6327;
    --gold-light: #d9bd6e;
    --cream: #e8e4d8;
    --cream-dim: #bdb8aa;
  }
  html, body {
    margin: 0;
    padding: 0;
    width: 1200px;
    height: 1200px;
    overflow: hidden;
    background: var(--paper);
  }
  .canvas {
    position: relative;
    width: 1200px;
    height: 1200px;
  }
  .label {
    position: absolute;
    left: 310px;
    top: 170px;
    width: 580px;
    height: 860px;
    background: var(--label-black);
    color: var(--cream);
    text-align: center;
    box-sizing: border-box;
    overflow: hidden;
  }
  .brand {
    position: absolute;
    top: 70px;
    left: 0;
    right: 0;
  }
  .brand-ornament {
    position: absolute;
    left: 110px;
    top: 20px;
    width: 360px;
    height: 170px;
    background: radial-gradient(ellipse at center, rgba(179,145,63,0.22), rgba(179,145,63,0) 70%);
  }
  .brand-lockup {
    position: relative;
    display: flex;
    justify-content: center;
    align-items: center;
    gap: 18px;
    margin-top: 48px;
  }
  .brand-name {
    font-family: "Cinzel", serif;
    font-weight: 700;
    font-size: 40px;
    letter-spacing: 2px;
    line-height: 1.1;
    color: var(--cream);
    text-align: center;
  }
  .brand-name span { display: block; }
  .brand-dot {
    flex: none;
    width: 36px;
    height: 36px;
    border-radius: 50%;
    border: 2px solid var(--gold);
    box-sizing: border-box;
  }
  .brand-tagline {
    position: relative;
    margin-top: 18px;
    font-family: "Cinzel", serif;
    font-weight: 500;
    font-size: 17px;
    letter-spacing: 4px;
    color: var(--cream-dim);
    text-transform: uppercase;
  }
  .product {
    position: absolute;
    left: 40px;
    right: 40px;
    top: 320px;
    height: 290px;
  }
  .product-frame {
    position: absolute;
    inset: 0;
  }
  .product-ornament {
    position: absolute;
    left: 0;
    top: 60px;
    width: 500px;
    height: 220px;
    background: linear-gradient(90deg, rgba(179,145,63,0.18), rgba(179,145,63,0) 18%, rgba(179,145,63,0) 82%, rgba(179,145,63,0.18));
  }
  .product-subtitle {
    position: absolute;
    top: 22px;
    left: 0;
    right: 0;
    font-family: "Cinzel", serif;
    font-weight: 700;
    font-size: 20px;
    letter-spacing: 2px;
    color: var(--cream);
    transform: rotate(-4deg);
  }
  .product-title {
    position: absolute;
    top: 110px;
    left: 0;
    right: 0;
    font-family: "Playfair Display", serif;
    font-weight: 800;
    font-size: 86px;
    letter-spacing: 4px;
    color: var(--cream);
    line-height: 1;
  }
  .product-flavor {
    position: absolute;
    top: 218px;
    left: 0;
    right: 0;
    font-family: "Cinzel", serif;
    font-weight: 700;
    font-size: 19px;
    letter-spacing: 4px;
    line-height: 24px;
    color: var(--cream);
  }
  .strength-rule {
    position: absolute;
    left: 210px;
    width: 160px;
    top: 648px;
    height: 0;
    border-top: 2px solid var(--gold);
  }
  .strength {
    position: absolute;
    left: 150px;
    width: 280px;
    top: 662px;
    height: 72px;
  }
  .strength-frame {
    position: absolute;
    inset: 0;
  }
  .strength-value {
    position: relative;
    font-family: "Old Standard TT", serif;
    font-weight: 700;
    font-size: 36px;
    line-height: 72px;
    color: var(--cream);
  }
  .volume {
    position: absolute;
    top: 780px;
    left: 0;
    right: 0;
    font-family: "Old Standard TT", serif;
    font-size: 20px;
    color: var(--cream-dim);
  }
</style>
</head>
<body>
<main class="canvas">
  <section class="label">
    <header class="brand">
      <div class="brand-ornament" role="img" aria-label="Gold filigree scrollwork surrounding the brand name"></div>
      <div class="brand-lockup">
        <div class="brand-name"><span>Thornwick</span><span>Meadows</span></div>
        <span class="brand-dot"></span>
      </div>
      <div class="brand-tagline">Verdant Curios</div>
    </header>

    <div class="product">
      <svg class="product-frame" viewBox="0 0 500 290" width="500" height="290" aria-hidden="true">
        <g fill="none" stroke="var(--gold)" stroke-width="2">
          <path d="M70 80 Q250 50 430 62"/>
          <path d="M40 90 Q20 170 40 250"/>
          <path d="M460 70 Q480 150 460 240"/>
          <path d="M60 262 Q250 254 440 262"/>
          <line x1="120" y1="100" x2="380" y2="96"/>
          <line x1="120" y1="208" x2="380" y2="206"/>
        </g>
      </svg>
      <div class="product-ornament" role="img" aria-label="Gold Victorian flourishes framing the product name"></div>
      <div class="product-subtitle">Full Spectrum Hemp Extract</div>
      <div class="product-title">CBD OIL</div>
      <div class="product-flavor">Natural Flavor</div>
    </div>

    <div class="strength-rule"></div>
    <div class="strength">
      <svg class="strength-frame" viewBox="0 0 280 72" width="280" height="72" aria-hidden="true">
        <rect x="4" y="4" width="272" height="64" rx="32" fill="none" stroke="var(--gold)" stroke-width="2"/>
      </svg>
      <div class="strength-value">1000 mg</div>
    </div>

    <div class="volume">1 fl oz. ( 30ml )</div>
  </section>
</main>
</body>
</html>
```